Business Card for Dental Surgery

Professional and vibrant business card for dental surgery

Other side to incorporate space for appointment date and times

My website is www.tallowbydental.com.au

Target Market(s)

All

Industry/Entity Type

Dental

Requirements
Must have
• Catchy
Phone no, internet etc
Nice to have
• portray same image as website.
on reverse appointment side:
"Please give 24 hours notice if you cannot attend"
Nice colours

```html
<!DOCTYPE html>
<html lang="en">
<head>
<meta charset="utf-8">
<title>Tallowby Dental – Business Card</title>
<link rel="stylesheet" href="https://fonts.googleapis.com/css2?family=Arimo:ital,wght@0,400;0,700;1,400&display=swap">
<style>
  :root{
    --purple:#a64df5;
    --lime:#a9f542;
    --ink:#2e2e2e;
    --text:#333333;
    --line:#b4f36a;
    --paper:#ffffff;
    --page:#ffffff;
    --icon:#6f6f6f;
    --icon-light:#f2f2f2;
  }
  *{box-sizing:border-box;margin:0;padding:0}
  html,body{width:918px;height:1200px;overflow:hidden;background:var(--page)}
  body{position:relative;font-family:"Arimo",Arial,sans-serif;color:var(--text)}

  .card{position:absolute;left:45px;width:826px;height:533px;background:var(--paper);border:1.5px solid #111;overflow:hidden}
  .card--front{top:46px}
  .card--back{top:626px}
  .band{position:absolute;top:0;bottom:0}
  .band--purple{left:0;width:38px;background:var(--purple)}
  .band--lime{left:38px;width:39px;background:var(--lime)}

  .brand{position:absolute;left:110px;font-weight:700;color:var(--purple);letter-spacing:-2px;white-space:nowrap;line-height:1}
  .card--front .brand{top:39px;font-size:80px}
  .tagline{position:absolute;left:110px;color:var(--purple);white-space:nowrap}
  .card--front .tagline{top:134px;font-size:31px}

  .photo{position:absolute}
  .photo--front{left:538px;top:177px;width:288px;height:356px;
    background:radial-gradient(ellipse at 55% 40%,#e8c1a6 0%,#f1dccd 38%,#e6edf3 70%,#ffffff 100%)}
  .photo--back{left:543px;top:175px;width:283px;height:358px;opacity:.35;
    background:radial-gradient(ellipse at 55% 40%,#e8c1a6 0%,#f1dccd 38%,#eef2f6 70%,#ffffff 100%)}

  .dentist-name{position:absolute;left:110px;top:212px;font-size:27px;font-weight:700;color:var(--ink);white-space:nowrap}
  .dentist-name small{font-size:17px;font-weight:400;margin-left:4px}
  .name-rule{position:absolute;left:110px;top:249px;width:349px;height:2px;background:var(--line)}
  .dentist-role{position:absolute;left:110px;top:256px;font-size:21px;color:var(--text)}
  .phone{position:absolute;left:110px;top:334px;font-size:21px;white-space:nowrap}
  .phone strong{font-size:31px;color:var(--purple);margin-left:2px}
  .web{position:absolute;left:110px;top:373px;font-size:31px;font-weight:700;color:var(--purple);white-space:nowrap;letter-spacing:-.3px}
  .address{position:absolute;left:110px;top:461px;font-size:19px;color:var(--text);white-space:nowrap}

  .calendar{position:absolute;left:110px;top:33px;width:86px;height:94px}
  .appt-title{position:absolute;left:207px;top:60px;font-size:38px;font-weight:700;color:var(--purple);white-space:nowrap}
  .appt-col{position:absolute;top:138px;font-size:20px;color:#111}
  .col-date{left:110px}
  .col-time{left:274px}
  .col-dentist{left:458px}
  .appt-rule{position:absolute;height:2px;background:var(--line)}
  .notice{position:absolute;left:110px;top:406px;font-size:19px;font-style:italic;line-height:30px;color:#111}
  .card--back .brand{left:338px;top:404px;font-size:52px;letter-spacing:-1.5px}
  .card--back .tagline{left:338px;top:468px;font-size:21px}
</style>
</head>
<body>

<section class="card card--front">
  <div class="band band--purple"></div>
  <div class="band band--lime"></div>
  <div class="photo photo--front" role="img" aria-label="Photo of a smiling young couple, woman riding piggyback on man"></div>
  <div class="brand">Tallowby Dental</div>
  <div class="tagline">high quality dental treatment you can afford</div>
  <div class="dentist-name">Dr Lena Marsh <small>BDS FRACDS</small></div>
  <div class="name-rule"></div>
  <div class="dentist-role">Implant and surgical dentist</div>
  <div class="phone">Telephone: <strong>02 9555 0142</strong></div>
  <div class="web">www.tallowbydental.com.au</div>
  <div class="address">18 Tallowby Road Tallowby NSW 2199</div>
</section>

<section class="card card--back">
  <div class="band band--purple"></div>
  <div class="band band--lime"></div>
  <div class="photo photo--back" role="img" aria-label="Faded photo of a smiling young couple"></div>

  <svg class="calendar" viewBox="0 0 86 94" aria-hidden="true">
    <rect x="4" y="12" width="78" height="78" rx="6" fill="var(--icon-light)" stroke="var(--icon)" stroke-width="3"/>
    <path d="M4 18a6 6 0 0 1 6-6h66a6 6 0 0 1 6 6v14H4z" fill="var(--purple)"/>
    <rect x="20" y="4" width="6" height="16" rx="3" fill="var(--icon)"/>
    <rect x="60" y="4" width="6" height="16" rx="3" fill="var(--icon)"/>
    <g fill="var(--icon)">
      <rect x="14" y="42" width="12" height="10" rx="1"/>
      <rect x="31" y="42" width="12" height="10" rx="1"/>
      <rect x="48" y="42" width="12" height="10" rx="1"/>
      <rect x="65" y="42" width="8" height="10" rx="1"/>
      <rect x="14" y="58" width="12" height="10" rx="1"/>
      <rect x="31" y="58" width="12" height="10" rx="1"/>
      <rect x="48" y="58" width="12" height="10" rx="1" fill="var(--purple)"/>
      <rect x="65" y="58" width="8" height="10" rx="1"/>
      <rect x="14" y="74" width="12" height="8" rx="1"/>
      <rect x="31" y="74" width="12" height="8" rx="1"/>
    </g>
  </svg>
  <div class="appt-title">appoinment time</div>

  <div class="appt-col col-date">Date</div>
  <div class="appt-col col-time">Time</div>
  <div class="appt-col col-dentist">Dentist</div>

  <div class="appt-rule" style="left:110px;top:172px;width:147px"></div>
  <div class="appt-rule" style="left:274px;top:172px;width:171px"></div>
  <div class="appt-rule" style="left:458px;top:172px;width:306px"></div>
  <div class="appt-rule" style="left:110px;top:227px;width:147px"></div>
  <div class="appt-rule" style="left:274px;top:227px;width:171px"></div>
  <div class="appt-rule" style="left:458px;top:227px;width:306px"></div>
  <div class="appt-rule" style="left:110px;top:282px;width:147px"></div>
  <div class="appt-rule" style="left:274px;top:282px;width:171px"></div>
  <div class="appt-rule" style="left:458px;top:282px;width:306px"></div>
  <div class="appt-rule" style="left:110px;top:336px;width:147px"></div>
  <div class="appt-rule" style="left:274px;top:336px;width:171px"></div>
  <div class="appt-rule" style="left:458px;top:336px;width:306px"></div>
  <div class="appt-rule" style="left:110px;top:391px;width:147px"></div>
  <div class="appt-rule" style="left:274px;top:391px;width:171px"></div>
  <div class="appt-rule" style="left:458px;top:391px;width:306px"></div>

  <p class="notice">Please give 24<br>hours notice if you<br>cannot attend.</p>
  <div class="brand">Tallowby Dental</div>
  <div class="tagline">high quality dental treatment you can afford</div>
</section>

</body>
</html>
```